Fund Harbor

We need desigin for our main page(concept will be used for other pages also).
We already have a logo, and moqup of our main page(see attch).
You could change layers and positions on moqup, but please use logo, and its colors in design creating. (We have logo in different colors, i attached 2 samples, so you could use also another colors if you wish).

Our bussinees will be something similar to LaunchPeak or Backwise.co, but with some special features. So main idea: start-ups, donations, investemnets

Designs were prefer:
http://backwise.co/
http://www.launchpeak.com/

Target Market(s)

Clients are middle aged persons, who interested in new start-ups, investments and so on.

Requirements
Must have
• Design must be neat

```html
<!DOCTYPE html>
<html lang="en">
<head>
<meta charset="utf-8">
<title>Fund Harbor</title>
<link href="https://fonts.googleapis.com/css2?family=Arimo:wght@400;700&family=Play:wght@400;700&display=swap" rel="stylesheet">
<style>
:root{
  --navy:#1f3d6e;
  --navy-dark:#142a4f;
  --navy-light:#3d64a0;
  --brand:#2f5aa0;
  --rust:#c2552e;
  --rust-dark:#9e3d1d;
  --page:#e9e9e9;
  --panel:#ffffff;
  --line:#dcdcdc;
  --text:#2b2b2b;
  --muted:#555;
  --footer:#3b3b3b;
  --link:#1a4d9c;
}
*{box-sizing:border-box;margin:0;padding:0}
html,body{width:1030px;height:1200px;overflow:hidden}
body{position:relative;background:var(--page);font-family:"Arimo",Arial,sans-serif;color:var(--text)}
.abs{position:absolute}
.header{left:0;top:0;width:1030px;height:118px;background:linear-gradient(#fbfbfb,#f3f3f3);border-bottom:1px solid #e2e2e2}
.brand{left:95px;top:48px;display:flex;align-items:center;gap:8px;font-family:"Play",sans-serif;font-weight:700;font-size:24px;color:var(--brand);letter-spacing:.5px}
.brand-mark{width:20px;height:20px;background:var(--navy);border-radius:50%}
.main-nav{left:343px;top:51px;width:368px;height:34px;border-radius:17px;background:linear-gradient(var(--navy-light),var(--navy-dark));border:2px solid #b8c4d8;display:flex;align-items:center;padding:0 4px;font-size:10.5px;color:#fff}
.main-nav span{flex:1;text-align:center}
.main-nav .active{flex:0 0 108px;height:24px;line-height:24px;background:#fff;color:var(--navy-dark);border-radius:12px;font-weight:700}
.search{left:758px;top:33px;width:183px;height:23px;border-radius:12px;background:#f1f1f1;border:1px solid #d6d6d6;font-size:11px;color:#999;line-height:21px;padding-left:24px}
.search svg{position:absolute;left:7px;top:5px}
.lang{left:826px;top:70px;width:115px;height:23px;border-radius:12px;background:#f1f1f1;border:1px solid #d6d6d6;font-size:11.5px;color:#888;line-height:21px;padding-left:10px}
.lang i{position:absolute;right:3px;top:2px;width:18px;height:17px;border-radius:50%;background:#1e1e1e}
.lang i::after{content:"";position:absolute;left:5px;top:5px;width:5px;height:5px;border-right:2px solid #fff;border-bottom:2px solid #fff;transform:rotate(45deg)}
.panel{background:var(--panel);border:1px solid #d4d4d4;border-radius:5px;box-shadow:0 1px 2px rgba(0,0,0,.06)}
.stats{left:87px;top:141px;width:204px;height:267px;padding:8px 0}
.stats li{list-style:none;height:34.5px;line-height:33px;border-bottom:1px solid var(--line);font-size:11px;padding-left:26px;position:relative;margin:0 4px}
.stats li:last-child{border-bottom:none}
.stats li svg{position:absolute;left:6px;top:12px}
.video{left:311px;top:139px;width:434px;height:272px;padding:3px;border-radius:6px}
.video-frame{position:relative;width:100%;height:248px;background:linear-gradient(135deg,#dfe6ec 0%,#b9c7d3 40%,#8fa3b4 70%,#cfd8de 100%);overflow:hidden}
.play-btn{position:absolute;left:172px;top:94px;width:62px;height:44px;background:rgba(40,40,40,.85);border-radius:3px}
.play-btn::after{content:"";position:absolute;left:23px;top:11px;border-left:20px solid #fff;border-top:11px solid transparent;border-bottom:11px solid transparent}
.video-bar{height:20px;background:linear-gradient(#f4f4f4,#d9d9d9);display:flex;align-items:center;font-size:7.5px;color:#444;padding:0 4px;gap:6px}
.video-bar .track{flex:1;height:5px;background:#ccc;border-radius:3px;position:relative}
.video-bar .track b{position:absolute;left:0;top:0;width:80%;height:5px;background:#d98a8a;border-radius:3px}
.tabs{left:770px;top:141px;display:flex;gap:2px;font-size:11.5px}
.tab{height:28px;line-height:28px;padding:0 14px;border-radius:6px 6px 0 0;background:#f4f4f4;border:1px solid #d4d4d4;color:#333}
.tab.active{background:linear-gradient(var(--navy-light),var(--navy-dark));color:#fff;border-color:var(--navy)}
.login{left:762px;top:168px;width:181px;height:240px;padding:30px 10px 0 10px;font-size:11px}
.login label{display:block;margin-bottom:7px}
.login .field{height:28px;background:#f0f0f0;border:1px solid #e0e0e0;border-radius:3px;margin-bottom:19px}
.login .forgot{font-size:10px;color:var(--link);text-decoration:underline;margin-top:-4px;margin-left:-1px;white-space:nowrap}
.btn-navy{background:linear-gradient(var(--navy-light),var(--navy-dark));color:#fff;font-weight:700;border-radius:3px;border:1px solid #0e1f3c;text-align:center}
.login .submit{position:absolute;left:77px;top:175px;width:86px;height:25px;line-height:23px;font-size:11.5px}
.login .save{position:absolute;left:12px;top:212px;font-size:10.5px;color:#444;display:flex;align-items:center;gap:6px}
.login .save i{width:11px;height:11px;border:1px solid #777;background:#fff;position:relative}
.login .save i::after{content:"";position:absolute;left:3px;top:0;width:3px;height:7px;border-right:2px solid #1a8a2c;border-bottom:2px solid #1a8a2c;transform:rotate(40deg)}
.ribbon{top:448px;width:184px;height:38px}
.ribbon span{position:absolute;left:18px;top:0;line-height:38px;font-family:"Play",sans-serif;font-weight:700;font-size:18px;color:#fff}
.card{top:513px;width:200px;height:382px;text-align:center}
.card h2{margin-top:8px;font-family:"Play",sans-serif;font-weight:400;font-size:23px;text-decoration:underline;text-underline-offset:3px;color:#222;height:30px}
.card .photo{margin:6px auto 0;width:184px;height:108px}
.card p{font-size:9.3px;line-height:15.5px;color:#444;padding:10px 14px 0;height:72px}
.progress{margin:11px auto 0;width:162px;height:17px;border-radius:9px;background:linear-gradient(#f7f7f7,#e6e6e6);border:1px solid #d8d8d8;position:relative}
.progress b{position:absolute;right:-1px;top:-1px;height:17px;width:72px;border-radius:9px;background:linear-gradient(var(--navy-light),var(--navy-dark));color:#fff;font-family:"Play",sans-serif;font-size:9.5px;line-height:17px}
.invested{margin:15px auto 0;width:103px;height:20px;line-height:20px;border-radius:3px;background:linear-gradient(#d7734a,var(--rust-dark));color:#fff;font-family:"Play",sans-serif;font-size:9.5px}
.pair{display:flex;justify-content:center;gap:6px;margin-top:15px}
.pair .btn-navy{height:24px;line-height:22px;font-family:"Play",sans-serif;font-size:11px;border:2px solid #c9d1de}
.invert{margin:11px auto 0;width:150px;height:32px;line-height:32px;border-radius:8px;background:linear-gradient(#ffffff,#dcdcdc);border:1px solid #cfcfcf;font-family:"Play",sans-serif;font-weight:700;font-size:18px;color:#444;letter-spacing:.5px}
.cta{left:379px;top:944px;width:293px;height:134px;border-radius:6px;background:linear-gradient(#ffffff,#e6e6e6);border:1px solid #d8d8d8;text-align:center;font-size:18px;color:#2b2b2b}
.cta h3{font-weight:700;font-size:18px;margin-top:20px;letter-spacing:.5px}
.cta .sub{margin-top:7px;letter-spacing:.3px}
.cta .yes{width:180px;height:29px;line-height:27px;margin:16px auto 0;border-radius:4px;font-size:14px}
.footer{left:0;top:1113px;width:1030px;height:87px;background:var(--footer);color:#fff;font-size:11.5px}
.footer .connect{position:absolute;left:95px;top:30px;display:flex;align-items:center;gap:6px}
.footer .connect span{margin-right:8px}
.footer .connect i{width:18px;height:18px;background:#ddd;border-radius:3px;display:block}
.footer .copy{position:absolute;left:95px;top:55px}
.footer .brand-foot{position:absolute;right:90px;top:40px;display:flex;align-items:center;gap:7px;font-family:"Play",sans-serif;font-weight:700;font-size:20px;color:#cfcfcf}
.footer .brand-foot i{width:16px;height:16px;background:#cfcfcf;border-radius:50%}
</style>
</head>
<body>

<header class="abs header"></header>
<div class="abs brand"><span class="brand-mark"></span>Fund Harbor</div>

<nav class="abs main-nav">
  <span class="active">How it Works ?</span>
  <span>Projects Review</span>
  <span>Virtual Office</span>
</nav>

<div class="abs search">
  <svg width="12" height="12" viewBox="0 0 12 12"><circle cx="5" cy="5" r="3.6" fill="none" stroke="#777" stroke-width="1.5"/><line x1="7.6" y1="7.6" x2="11" y2="11" stroke="#777" stroke-width="2"/></svg>
  Search
</div>
<div class="abs lang">English<i></i></div>

<ul class="abs panel stats">
  <li><svg width="12" height="10" viewBox="0 0 12 10"><path d="M0 3h6V0l6 5-6 5V7H0z" fill="#3b5cc4"/></svg>$ 50 000 000 of Investment</li>
  <li><svg width="12" height="10" viewBox="0 0 12 10"><path d="M0 3h6V0l6 5-6 5V7H0z" fill="#3b5cc4"/></svg>1600 Starts- ups</li>
  <li><svg width="12" height="10" viewBox="0 0 12 10"><path d="M0 3h6V0l6 5-6 5V7H0z" fill="#3b5cc4"/></svg>700 Orgnization</li>
  <li><svg width="12" height="10" viewBox="0 0 12 10"><path d="M0 3h6V0l6 5-6 5V7H0z" fill="#3b5cc4"/></svg>10 000 Investors</li>
  <li><svg width="12" height="10" viewBox="0 0 12 10"><path d="M0 3h6V0l6 5-6 5V7H0z" fill="#3b5cc4"/></svg>5000 Employees</li>
  <li><svg width="12" height="10" viewBox="0 0 12 10"><path d="M0 3h6V0l6 5-6 5V7H0z" fill="#3b5cc4"/></svg>2000 Partners</li>
  <li><svg width="12" height="10" viewBox="0 0 12 10"><path d="M0 3h6V0l6 5-6 5V7H0z" fill="#3b5cc4"/></svg>$ 10 000 000 of Profit</li>
</ul>

<div class="abs panel video">
  <div class="video-frame" role="img" aria-label="Video still: three business people smiling around a laptop in a bright office">
    <svg class="abs" style="right:0;top:0" width="120" height="120" viewBox="0 0 120 120">
      <polygon points="30,0 58,0 120,62 120,90" fill="#c0422a"/>
      <text x="0" y="0" transform="translate(52,12) rotate(45)" font-family="Georgia,serif" font-size="12" fill="#fff">Watch the Video</text>
    </svg>
    <div class="play-btn"></div>
  </div>
  <div class="video-bar">
    <svg width="9" height="10" viewBox="0 0 9 10"><path d="M0 0l9 5-9 5z" fill="#333"/></svg>
    <svg width="14" height="10" viewBox="0 0 14 10"><path d="M0 3h3l4-3v10L3 7H0z" fill="#333"/><path d="M9 3v4M11 2v6" stroke="#333"/></svg>
    <span>0:00 / 3:13</span>
    <div class="track"><b></b></div>
    <span>480p</span>
    <svg width="14" height="9" viewBox="0 0 14 9"><rect width="14" height="9" rx="2" fill="#444"/><path d="M4 6l3-3 3 3z" fill="#fff"/></svg>
    <svg width="10" height="10" viewBox="0 0 10 10"><path d="M4 0h2v4h4v2H6v4H4V6H0V4h4z" fill="#333"/></svg>
    <svg width="12" height="10" viewBox="0 0 12 10"><path d="M0 3V0h3M9 0h3v3M12 7v3H9M3 10H0V7" fill="none" stroke="#333" stroke-width="1.5"/></svg>
  </div>
</div>

<div class="abs tabs"><span class="tab active">Login</span><span class="tab">Registration</span></div>
<form class="abs panel login">
  <label>Email or Phone</label>
  <div class="field"></div>
  <label>Password</label>
  <div class="field"></div>
  <div class="forgot">Forgot the Password ?</div>
  <div class="btn-navy submit">Login Area</div>
  <div class="save"><i></i>Save login</div>
</form>

<div class="abs ribbon" style="left:88px">
  <svg width="184" height="38" viewBox="0 0 184 38"><defs><linearGradient id="rg" x1="0" y1="0" x2="0" y2="1"><stop offset="0" stop-color="#3d64a0"/><stop offset="1" stop-color="#142a4f"/></linearGradient></defs><path d="M4 0h162l18 19-18 19H4a4 4 0 0 1-4-4V4a4 4 0 0 1 4-4z" fill="url(#rg)" stroke="#c9d1de" stroke-width="2"/></svg>
  <span>Recommended</span>
</div>
<div class="abs ribbon" style="left:310px">
  <svg width="184" height="38" viewBox="0 0 184 38"><path d="M4 0h162l18 19-18 19H4a4 4 0 0 1-4-4V4a4 4 0 0 1 4-4z" fill="url(#rg)" stroke="#c9d1de" stroke-width="2"/></svg>
  <span>Popular</span>
</div>
<div class="abs ribbon" style="left:526px">
  <svg width="184" height="38" viewBox="0 0 184 38"><path d="M4 0h162l18 19-18 19H4a4 4 0 0 1-4-4V4a4 4 0 0 1 4-4z" fill="url(#rg)" stroke="#c9d1de" stroke-width="2"/></svg>
  <span>Most invesed</span>
</div>
<div class="abs ribbon" style="left:743px">
  <svg width="184" height="38" viewBox="0 0 184 38"><path d="M4 0h162l18 19-18 19H4a4 4 0 0 1-4-4V4a4 4 0 0 1 4-4z" fill="url(#rg)" stroke="#c9d1de" stroke-width="2"/></svg>
  <span>New</span>
</div>

<article class="abs panel card" style="left:87px">
  <h2>Project A</h2>
  <div class="photo" role="img" aria-label="Photo: businessmen shaking hands in an office" style="background:linear-gradient(135deg,#3a3f48,#8a96a6 50%,#2a2d33)"></div>
  <p>Lorem Ipsum is simply dummy text of the printing and typesetting industry. Lorem Ipsum has been simply dummy text of the printing.</p>
  <div class="progress"><b>70% success</b></div>
  <div class="invested">$90 000 invested</div>
  <div class="pair"><span class="btn-navy" style="width:86px">200 Invertor</span><span class="btn-navy" style="width:78px">23 Day left</span></div>
  <div class="invert">INVERT</div>
</article>

<article class="abs panel card" style="left:307px">
  <h2>Project B</h2>
  <div class="photo" role="img" aria-label="Photo: hands dropping a coin into a piggy bank" style="background:linear-gradient(160deg,#b35a2a,#e8b48a 45%,#f2efea 75%)"></div>
  <p>Lorem Ipsum is simply dummy text of the printing and typesetting industry. Lorem Ipsum has been simply dummy text of the printing.</p>
  <div class="progress"><b>70% success</b></div>
  <div class="invested">$90 000 invested</div>
  <div class="pair"><span class="btn-navy" style="width:86px">200 Invertor</span><span class="btn-navy" style="width:78px">23 Day left</span></div>
  <div class="invert">INVERT</div>
</article>

<article class="abs panel card" style="left:526px">
  <h2>Project C</h2>
  <div class="photo" role="img" aria-label="Illustration: business figures climbing rising steps over a world map" style="background:linear-gradient(180deg,#e7e9ec,#b9bec6 70%,#8e949d)"></div>
  <p>Lorem Ipsum is simply dummy text of the printing and typesetting industry. Lorem Ipsum has been simply dummy text of the printing.</p>
  <div class="progress"><b>70% success</b></div>
  <div class="invested">$90 000 invested</div>
  <div class="pair"><span class="btn-navy" style="width:86px">200 Invertor</span><span class="btn-navy" style="width:78px">23 Day left</span></div>
  <div class="invert">INVERT</div>
</article>

<article class="abs panel card" style="left:745px">
  <h2>Project D</h2>
  <div class="photo" role="img" aria-label="Photo: presenter showing a growth chart to a meeting" style="background:linear-gradient(180deg,#6f8fb5,#dfe5ec 45%,#4a4f57)"></div>
  <p>Lorem Ipsum is simply dummy text of the printing and typesetting industry. Lorem Ipsum has been simply dummy text of the printing.</p>
  <div class="progress"><b>70% success</b></div>
  <div class="invested">$90 000 invested</div>
  <div class="pair"><span class="btn-navy" style="width:86px">200 Invertor</span><span class="btn-navy" style="width:78px">23 Day left</span></div>
  <div class="invert">INVERT</div>
</article>

<section class="abs cta">
  <h3>View all projects ?</h3>
  <div class="sub">More then 1000 projects</div>
  <div class="btn-navy yes">YES</div>
</section>

<footer class="abs footer">
  <div class="connect"><span>Stay Connected</span><i></i><i></i><i></i></div>
  <div class="copy">Copyright © 2013 Fund Harbor, LLC. All rights reserved.</div>
  <div class="brand-foot"><i></i>Fund Harbor</div>
</footer>

</body>
</html>
```